Business Card Design

We need a business card design for our new expansion based in Bloomfield Hills, Michigan. Our company is Quiet Harbor Institute & Wellness Center. Our Academy teaches individuals of all ages and professions to live from their soul. We teach intuitive development, meditation and mindfulness; shamanic healing. And ourr healing center provides holistic services. We offer certification programs that support the ethical practices of Intuitive professionals. Our team of Intuitive Practitioners includes: doctors, psychologists, chiropractor, soul retrievers, mediums, etc who all balance their knowledge with intuitive wisdom.

We want our symbol to be the Blue Morpho Buttefly and the colors on the card to complement it. We want to communicate inspiration, healing and empowerment. Thank you
Updates

Industry/Entity Type

Business

Contact Information for Business Card

Dana Orwick
Medium. Author. Soul Retriever.
Founder, Quiet Harbor

Quiet Harbor

19 North Cedar Mill Drive Suite 100
Fernwood Heights, MI 48517
248-603-7418

www.danaorwick.example

Requirements
Must have
• blue morpho butterfly

```html
<!DOCTYPE html>
<html lang="en">
<head>
<meta charset="utf-8">
<title>Quiet Harbor – Business Card</title>
<link rel="stylesheet" href="https://fonts.googleapis.com/css2?family=Montserrat:wght@500;600;700&family=Parisienne&display=swap">
<style>
  :root {
    --navy: #1c355e;
    --paper: #ffffff;
    --canvas: #f4f5f7;
    --morpho-light: #5fa2f0;
    --morpho-deep: #1f4fb8;
    --ink-soft: #e6ecf5;
  }
  html, body {
    margin: 0;
    width: 1200px;
    height: 702px;
    overflow: hidden;
    background: var(--canvas);
  }
  .stage {
    position: relative;
    width: 1200px;
    height: 702px;
  }
  .card {
    position: absolute;
    top: 200px;
    width: 520px;
    height: 297px;
    box-shadow: 0 6px 18px rgba(0,0,0,.18);
    overflow: hidden;
  }

  /* Front */
  .card--front { left: 50px; background: var(--paper); }
  .front__butterfly {
    position: absolute;
    left: 70px;
    top: 58px;
    width: 190px;
    height: 150px;
    border-radius: 46% 46% 40% 40% / 55% 55% 45% 45%;
    background: radial-gradient(ellipse at 50% 45%, var(--morpho-light) 0%, var(--morpho-deep) 75%, #18305f 100%);
  }
  .front__name {
    position: absolute;
    left: 285px;
    top: 105px;
    margin: 0;
    font-family: "Parisienne", cursive;
    font-weight: 400;
    font-size: 38px;
    color: var(--navy);
    letter-spacing: 1px;
  }
  .front__band {
    position: absolute;
    left: 0;
    bottom: 0;
    width: 520px;
    height: 56px;
  }
  .front__web {
    position: absolute;
    right: 34px;
    bottom: 18px;
    margin: 0;
    font-family: "Montserrat", sans-serif;
    font-weight: 600;
    font-size: 14px;
    letter-spacing: 4px;
    color: var(--paper);
  }

  /* Back */
  .card--back { left: 630px; background: var(--navy); color: var(--paper); }
  .back__name {
    position: absolute;
    top: 112px;
    left: 0;
    right: 0;
    margin: 0;
    text-align: center;
    font-family: "Montserrat", sans-serif;
    font-weight: 600;
    font-size: 25px;
    letter-spacing: 5px;
  }
  .back__roles {
    position: absolute;
    top: 150px;
    left: 0;
    right: 0;
    margin: 0;
    text-align: center;
    font-family: "Montserrat", sans-serif;
    font-weight: 600;
    font-size: 10px;
    letter-spacing: 1.8px;
    color: var(--ink-soft);
  }
  .back__strip {
    position: absolute;
    left: 0;
    bottom: 0;
    width: 520px;
    height: 40px;
  }
  .back__contact {
    position: absolute;
    left: 0;
    right: 0;
    bottom: 6px;
    margin: 0;
    text-align: center;
    font-family: "Montserrat", sans-serif;
    font-weight: 700;
    font-size: 8.5px;
    letter-spacing: 1px;
    line-height: 15px;
    color: var(--navy);
  }
  .contact__item { display: inline-flex; align-items: center; gap: 5px; margin: 0 6px; }
  .contact__icon { width: 9px; height: 9px; fill: var(--navy); }
</style>
</head>
<body>
<main class="stage">

  <section class="card card--front" aria-label="Card front">
    <div class="front__butterfly" role="img" aria-label="Blue morpho butterfly with open wings"></div>
    <h1 class="front__name">Quiet Harbor</h1>
    <svg class="front__band" viewBox="0 0 520 56" aria-hidden="true">
      <polygon points="0,56 40,0 520,0 520,56" fill="var(--navy)"/>
    </svg>
    <p class="front__web">www.danaorwick.example</p>
  </section>

  <section class="card card--back" aria-label="Card back">
    <h2 class="back__name">DANA ORWICK</h2>
    <p class="back__roles">founder | medium | author | soul retriever</p>
    <svg class="back__strip" viewBox="0 0 520 40" aria-hidden="true">
      <polygon points="0,0 520,0 492,40 28,40" fill="var(--paper)"/>
    </svg>
    <address class="back__contact">
      <span class="contact__item">
        <svg class="contact__icon" viewBox="0 0 10 10"><path d="M5 0a3.4 3.4 0 0 0-3.4 3.4C1.6 6 5 10 5 10s3.4-4 3.4-6.6A3.4 3.4 0 0 0 5 0zm0 4.8a1.4 1.4 0 1 1 0-2.8 1.4 1.4 0 0 1 0 2.8z"/></svg>
        19 North Cedar Mill Drive Suite 100 Fernwood Heights, MI 48517
      </span><br>
      <span class="contact__item">
        <svg class="contact__icon" viewBox="0 0 10 10"><path d="M2 0l2 2.2-1 1.3a6 6 0 0 0 3.5 3.5l1.3-1L10 8l-1.2 1.6C4.5 10 0 5.5.4 1.2z"/></svg>
        (248)-603-7418
      </span>
      <span class="contact__item">
        <svg class="contact__icon" viewBox="0 0 10 10"><path d="M0 2h10v6H0zM0 2l5 3.5L10 2" stroke="#fff" stroke-width=".8"/></svg>
        QuietHarbor444@mail.example
      </span>
    </address>
  </section>

</main>
</body>
</html>
```